We need a laundry sheet packingbox desgin

-look at our website plooimoes.nl to be in line with our house style/collor
We are a perfume seller and would like to offer also wasshingsheets with NO SMELL, so the customers can buy this incombination with our washingperfumes.
-the wassingheets will be neutrale(NO SMELL)
-it will be for the Dutch market
The next points should be on the desgin of the package
-our brand name: PLOOIMOES
-product name: WASSTRIPS
-(contains) Bevat: 30 wasstrips
-30 wasstrips = 60 wasbeurten
Please take some inspiration of others sellers & regarding eco friendly symbols etc.:
velunta.com & doxamp.nl
Backside information will be provided afther we found the right desgin
Please look at attachement pdf open box.
Here you can find the pdf design where you need to customize:
https://fy.qo/t-Lr8KxPq2Zh

```html
<!DOCTYPE html>
<html lang="nl">
<head>
<meta charset="utf-8">
<title>PLOOIMOES Wasstrips – verpakking bovenkant</title>
<link rel="stylesheet" href="https://fonts.googleapis.com/css2?family=Anton&family=Cinzel:wght@500&family=Montserrat:wght@700;800&family=Oswald:wght@600&display=swap">
<style>
  :root {
    --green: #4f9e31;
    --green-dark: #3f8a25;
    --kraft: #c9a27a;
    --kraft-light: #d3ae86;
    --white: #ffffff;
    --bg-top: #f6f6f6;
    --bg-bottom: #e4e4e4;
  }
  * { margin: 0; padding: 0; box-sizing: border-box; }
  html, body { width: 1200px; height: 1054px; overflow: hidden; }
  body {
    background: linear-gradient(160deg, var(--bg-top), var(--bg-bottom));
    display: flex; align-items: center; justify-content: center;
  }
  .box-lid { width: 960px; height: 640px; display: block; }
  .seal-text { font-family: "Montserrat", sans-serif; font-weight: 700; font-size: 15px; letter-spacing: 2px; fill: var(--white); }
  .flavour-tab-text { font-family: "Montserrat", sans-serif; font-weight: 800; font-size: 40px; letter-spacing: 5px; fill: var(--white); }
  .brand-name { font-family: "Cinzel", serif; font-weight: 500; font-size: 34px; letter-spacing: 2px; fill: var(--white); }
  .product-name { font-family: "Anton", sans-serif; font-size: 150px; fill: var(--green); stroke: var(--white); stroke-width: 6px; paint-order: stroke; letter-spacing: 2px; }
  .claim-label { font-family: "Oswald", sans-serif; font-weight: 600; font-size: 17px; letter-spacing: 1px; fill: var(--white); }
  .icon-line { fill: none; stroke: var(--white); stroke-width: 3.5; stroke-linejoin: round; stroke-linecap: round; }
</style>
</head>
<body>
<svg class="box-lid" viewBox="0 0 960 640" xmlns="http://www.w3.org/2000/svg" aria-label="Bovenkant verpakking PLOOIMOES Wasstrips neutraal">
  <defs>
    <path id="seal-arc-top" d="M-48,0 A48,48 0 0 1 48,0"/>
    <path id="seal-arc-bottom" d="M-54,0 A54,54 0 0 0 54,0"/>
    <path id="seal-arc-full" d="M-50,-8 A50,50 0 1 0 40,-30"/>
  </defs>

  <!-- kraft surface -->
  <rect class="lid-surface" width="960" height="640" fill="var(--kraft)"/>

  <!-- flavour tab -->
  <g class="flavour-tab">
    <path d="M520,0 H900 C880,40 860,60 820,60 H560 C535,60 520,40 520,0 Z" fill="var(--green)"/>
    <text class="flavour-tab-text" x="708" y="45" text-anchor="middle">NEUTRALE</text>
  </g>

  <!-- green bottom band -->
  <path class="lid-band" d="M0,240 H150 C215,240 235,290 235,340 V430 C235,475 260,495 310,495 H640 C690,495 712,470 730,440 C750,405 780,395 825,395 H960 V640 H0 Z"
        fill="var(--green)" stroke="var(--white)" stroke-width="5"/>

  <!-- seal: contents -->
  <g class="seal seal-contents" transform="translate(130,110)">
    <circle r="66" fill="var(--green)"/>
    <circle r="68" fill="none" stroke="var(--green)" stroke-width="10" stroke-dasharray="6 5"/>
    <circle r="56" fill="none" stroke="var(--white)" stroke-width="2"/>
    <text class="seal-text"><textPath href="#seal-arc-top" startOffset="50%" text-anchor="middle">BEVAT</textPath></text>
    <text class="seal-text"><textPath href="#seal-arc-bottom" startOffset="50%" text-anchor="middle">30 WASSTRIPS</textPath></text>
    <g class="icon-line" transform="translate(0,2)">
      <path d="M-22,-6 L0,-16 L22,-6 L0,4 Z"/>
      <path d="M-22,2 L0,12 L22,2"/>
      <path d="M-22,10 L0,20 L22,10"/>
    </g>
  </g>

  <!-- seal: washes -->
  <g class="seal seal-washes" transform="translate(830,235)">
    <circle r="66" fill="var(--green)"/>
    <circle r="68" fill="none" stroke="var(--green)" stroke-width="10" stroke-dasharray="6 5"/>
    <circle r="56" fill="none" stroke="var(--white)" stroke-width="2"/>
    <text class="seal-text"><textPath href="#seal-arc-bottom" startOffset="50%" text-anchor="middle">60 WASBEURTEN</textPath></text>
    <g class="icon-line" transform="translate(0,-10)">
      <rect x="-20" y="-22" width="40" height="44" rx="4"/>
      <line x1="-20" y1="-12" x2="20" y2="-12"/>
      <circle cx="0" cy="5" r="11"/>
    </g>
  </g>

  <!-- brand -->
  <g class="brand">
    <circle cx="480" cy="140" r="40" fill="none" stroke="var(--white)" stroke-width="5"/>
    <text class="brand-name" x="480" y="238" text-anchor="middle">PLOOIMOES</text>
  </g>

  <!-- product name -->
  <text class="product-name" x="470" y="425" text-anchor="middle" transform="rotate(8 470 370)">WASSTRIPS</text>

  <!-- claims -->
  <g class="claim claim-plastic-free" transform="translate(150,505)">
    <circle cx="0" cy="0" r="30" fill="var(--green-dark)" role="img" aria-label="Icoon walvis met golf, plasticvrij"/>
    <text class="claim-label" x="0" y="55" text-anchor="middle">PLASTIC FREE</text>
  </g>
  <g class="claim claim-biodegradable" transform="translate(330,535)">
    <path class="icon-line" d="M0,30 V0 M0,5 C-20,0 -30,-20 -26,-38 C-8,-32 2,-18 0,5 M0,10 C15,-12 40,-15 55,-8 C40,8 20,12 0,10"/>
    <text class="claim-label" x="0" y="60" text-anchor="middle">BIODEGRADABLE</text>
  </g>
  <g class="claim claim-clean" transform="translate(530,560)">
    <g class="icon-line">
      <path d="M0,-30 L6,-12 L22,-8 L6,-4 L0,14 L-6,-4 L-22,-8 L-6,-12 Z"/>
      <path d="M28,8 L31,16 L38,18 L31,20 L28,28 L25,20 L18,18 L25,16 Z"/>
      <path d="M-20,18 L-17,24 L-11,26 L-17,28 L-20,34 L-23,28 L-29,26 L-23,24 Z"/>
    </g>
    <text class="claim-label" x="0" y="60" text-anchor="middle">POWERFULL CLEAN</text>
  </g>
</svg>
</body>
</html>
```